Heronby Mortgage Capital Business Card

We need a business card design for our mortgage servicing company. In addition to servicing the loans of homeowners, we help homeowners with purchasing their homes and any mortgage refinancing. We would like to see designs that use the colors in the logo attached below (gold-ish yellow and navy blue), and any other design you deem fit! The design should communicate a simpler life with smart mortgages provided by Heronby.

```html
<!DOCTYPE html>
<html lang="en">
<head>
<meta charset="utf-8">
<title>Heronby Mortgage Capital – Business Card</title>
<link rel="stylesheet" href="https://fonts.googleapis.com/css2?family=Lato:wght@400;700;900&display=swap">
<style>
  :root {
    --backdrop: #717171;
    --navy: #27215a;
    --navy-light: #3a3470;
    --gold: #dfb23e;
    --card-shadow: 0 8px 22px rgba(0, 0, 0, 0.28);
  }
  * { margin: 0; padding: 0; box-sizing: border-box; }
  html, body {
    width: 1200px;
    height: 1000px;
    overflow: hidden;
    background: var(--backdrop);
    font-family: "Lato", sans-serif;
  }
  .stage { position: relative; width: 1200px; height: 1000px; }

  .card {
    position: absolute;
    width: 613px;
    height: 352px;
    box-shadow: var(--card-shadow);
  }

  .card-front {
    left: 292px;
    top: 117px;
    background: var(--navy);
    overflow: hidden;
  }
  .front-texture {
    position: absolute;
    inset: 0;
    background: linear-gradient(180deg, var(--navy) 0%, var(--navy-light) 45%, var(--navy-light) 60%, var(--navy) 100%);
  }
  .front-wordmark {
    position: absolute;
    left: 0;
    right: 0;
    top: 124px;
    text-align: center;
    font-weight: 900;
    font-size: 84px;
    line-height: 1;
    color: var(--gold);
    letter-spacing: -1px;
  }

  .card-back {
    left: 294px;
    top: 542px;
    background: var(--gold);
    color: var(--navy);
    text-align: center;
  }
  .back-brand {
    position: absolute;
    left: 0;
    right: 0;
    top: 54px;
    display: flex;
    justify-content: center;
    align-items: center;
    gap: 10px;
  }
  .brand-dot {
    width: 14px;
    height: 14px;
    border-radius: 50%;
    background: var(--navy);
  }
  .brand-name {
    font-weight: 900;
    font-size: 36px;
    line-height: 1;
    color: var(--navy);
  }
  .person-name {
    position: absolute;
    left: 0; right: 0;
    top: 145px;
    font-weight: 700;
    font-size: 24px;
    letter-spacing: 0.4px;
  }
  .person-role {
    position: absolute;
    left: 0; right: 0;
    top: 179px;
    font-size: 16px;
    letter-spacing: 0.6px;
  }
  .contact {
    position: absolute;
    left: 0; right: 0;
    top: 222px;
    font-size: 15.5px;
    line-height: 19px;
    letter-spacing: 0.8px;
    list-style: none;
  }
  .address {
    position: absolute;
    left: 0; right: 0;
    top: 303px;
    font-size: 15.5px;
    letter-spacing: 0.8px;
    font-style: normal;
  }
</style>
</head>
<body>
  <main class="stage">
    <section class="card card-front">
      <div class="front-texture" role="img" aria-label="Faint repeated brand-name pattern in muted violet on navy"></div>
      <div class="front-wordmark">Heronby</div>
    </section>

    <section class="card card-back">
      <div class="back-brand">
        <span class="brand-dot"></span>
        <span class="brand-name">Heronby</span>
      </div>
      <h1 class="person-name">Name Surname</h1>
      <p class="person-role">Position</p>
      <ul class="contact">
        <li>(888)-555-0174</li>
        <li>info@heronbymtg.com</li>
      </ul>
      <address class="address">418 3rd Ave N, Bayview, FL 33712</address>
    </section>
  </main>
</body>
</html>
```